Market Research firm needs updated business cards with new logo

We need the logo to be included somewhere on the card (attached). We would also like the phrases "Independent, Objective, Comprehensive" and "Research You Can Trust" somewhere on the card. Front or back. Our colors are hex codes 6075a7, e48d25 and 5a5b5b. Though you are certainly not limited to those shades, whatever you produce should coordinate with them. I have also attached our favicon. Feel free to use it in your design, but please do not use it to replace the full logo.

Contact Information for Business Card

see project description

Other font styles liked:
• Open Sans

Requirements
Must have
• the logo
• We use Open Sans font

```html
<!DOCTYPE html>
<html lang="en">
<head>
<meta charset="UTF-8">
<title>Kestrel Research – Business Card</title>
<link href="https://fonts.googleapis.com/css2?family=Open+Sans:wght@400;600;700&display=swap" rel="stylesheet">
<style>
  :root {
    --bg-top: #aab2bc;
    --bg-bottom: #454c56;
    --slate: #6b7888;
    --orange: #f07f1e;
    --ink: #5a5b5b;
    --white: #ffffff;
  }
  * { box-sizing: border-box; margin: 0; padding: 0; }
  html, body { width: 1200px; height: 895px; overflow: hidden; }
  body {
    font-family: "Open Sans", sans-serif;
    background: linear-gradient(180deg, var(--bg-top) 0%, var(--bg-bottom) 100%);
    position: relative;
  }
  .card {
    position: absolute;
    top: 297px;
    width: 520px;
    height: 300px;
    border-radius: 22px;
    box-shadow: 0 14px 30px rgba(0,0,0,0.35);
    overflow: hidden;
  }
  /* Back side */
  .card-back { left: 60px; background: var(--slate); color: var(--white); }
  .card-back .brand {
    position: absolute; right: 40px; bottom: 92px;
    display: flex; align-items: center; gap: 10px;
  }
  .brand-dot {
    width: 16px; height: 16px; border-radius: 50%; background: var(--orange);
  }
  .card-back .brand-name {
    font-size: 34px; font-weight: 400; letter-spacing: -0.5px; color: var(--white);
  }
  .values {
    position: absolute; right: 40px; bottom: 58px;
    font-size: 13px; letter-spacing: 0.8px;
  }
  .values .sep { color: var(--orange); margin: 0 8px; }

  /* Front side */
  .card-front { left: 620px; background: var(--white); color: var(--ink); }
  .card-front .brand {
    position: absolute; right: 34px; top: 30px;
    writing-mode: vertical-rl;
    display: flex; align-items: center; gap: 10px;
  }
  .card-front .brand-name {
    font-size: 32px; font-weight: 400; letter-spacing: -0.5px; color: var(--ink);
  }
  .person { position: absolute; left: 44px; top: 74px; }
  .person-name { font-size: 30px; font-weight: 600; color: var(--orange); line-height: 1.1; }
  .person-role { font-size: 15px; margin-top: 4px; letter-spacing: 0.5px; }
  .contacts { position: absolute; left: 44px; top: 160px; list-style: none; }
  .contacts li {
    display: flex; align-items: center; gap: 10px;
    font-size: 14px; letter-spacing: 0.4px; line-height: 24px;
  }
  .contacts svg { width: 14px; height: 14px; flex: none; }
  .contacts .accent { color: var(--orange); }
  .slogan {
    position: absolute; left: 44px; top: 248px;
    font-size: 14px; letter-spacing: 2px;
  }
</style>
</head>
<body>
  <section class="card card-back" aria-label="Card back">
    <div class="brand">
      <span class="brand-dot"></span>
      <span class="brand-name">Kestrel Research</span>
    </div>
    <p class="values">Independent<span class="sep">|</span>Objective<span class="sep">|</span>Comprehensive</p>
  </section>

  <section class="card card-front" aria-label="Card front">
    <div class="brand">
      <span class="brand-dot"></span>
      <span class="brand-name">Kestrel Research</span>
    </div>
    <div class="person">
      <h1 class="person-name">Daniel Hart</h1>
      <p class="person-role">CEO</p>
    </div>
    <ul class="contacts">
      <li>
        <svg viewBox="0 0 14 14" aria-hidden="true"><rect x="3" y="1" width="8" height="12" rx="1.5" fill="none" stroke="#f07f1e" stroke-width="1.6"/><line x1="6" y1="11" x2="8" y2="11" stroke="#f07f1e" stroke-width="1.4"/></svg>
        <span>000 000 0000</span>
      </li>
      <li>
        <svg viewBox="0 0 14 14" aria-hidden="true"><rect x="1" y="3" width="12" height="8" rx="1" fill="none" stroke="#f07f1e" stroke-width="1.6"/><polyline points="1.5,3.5 7,8 12.5,3.5" fill="none" stroke="#f07f1e" stroke-width="1.4"/></svg>
        <span>dhart@<span class="accent">kestrelresearch</span>.com</span>
      </li>
      <li>
        <svg viewBox="0 0 14 14" aria-hidden="true"><circle cx="8" cy="6" r="4.2" fill="none" stroke="#f07f1e" stroke-width="1.6"/><line x1="5" y1="9" x2="1.5" y2="12.5" stroke="#f07f1e" stroke-width="1.6"/></svg>
        <span>www.<span class="accent">kestrelresearch</span>.com</span>
      </li>
    </ul>
    <p class="slogan">Research You Can Trust</p>
  </section>
</body>
</html>
```